Label design for Cargo Pants.

We need modern packaging design for men's cargo pant for a brand name Vantu. All kinds of packaging designs are welcome.

The pant is folded and packaged in a poly bag. We require a label design for the brand name Vantu. The main label will be attached by a string on the belt loop. the size of that label will 25cm in length and 10cm wide. This is the first label the customer see's when he picks up the garment. Therefore, we require an eye catching design for that. If required it could have certain information about the chino pant on the main label such as Comfort fit, Wrinkle-resistant, machine washable, luxury fabric. But, if you feel that adding the above information spoils the design of the label then it is not a must to include the above information. On the back of the label we like to include the information that this pant was manufactured in an Quarv Platinum certified green plant and hence the damage to the environment because of the plant is nill.

The second label is attached on to the waist band and the purpose of that label is to include the size of the pant such 32x32. The size of that label is 8cm in length and 4cm in width. There is no design on the back on this label it has to be blank.

Sample, is provided for what we use for our chino pant.

```html
<!DOCTYPE html>
<html lang="en">
<head>
<meta charset="utf-8">
<title>Vantu Cargo Labels</title>
<link rel="stylesheet" href="https://fonts.googleapis.com/css2?family=Rubik+Dirt&family=Oswald:wght@500;600;700&family=Saira+Stencil+One&family=Big+Shoulders+Stencil+Display:wght@800;900&display=swap">
<style>
  :root {
    --backdrop: #eeeeef;
    --label-red: #de4f2f;
    --label-red-dark: #c8432a;
    --ink: #1a0f0c;
    --chalk: #fbf3ee;
    --grommet: #d9d9d9;
    --grommet-rim: #8d8d8d;
  }
  * { box-sizing: border-box; margin: 0; padding: 0; }
  html, body { width: 1200px; height: 1200px; overflow: hidden; }
  body { background: var(--backdrop); position: relative; font-family: "Oswald", sans-serif; }

  .label {
    position: absolute;
    overflow: hidden;
    background: linear-gradient(180deg, var(--label-red) 0%, var(--label-red-dark) 100%);
    box-shadow: 0 4px 10px rgba(0,0,0,.25);
  }
  .label--front { left: 76px; top: 86px; width: 410px; height: 1028px; }
  .label--back  { left: 524px; top: 86px; width: 410px; height: 1028px; }
  .label--size  { left: 970px; top: 432px; width: 164px; height: 322px; }

  .grommet {
    position: absolute; width: 26px; height: 26px; border-radius: 50%;
    background: var(--grommet); border: 3px solid var(--grommet-rim);
  }
  .grommet--tl { left: 10px; top: 10px; }
  .grommet--tr { right: 10px; top: 10px; }
  .grommet--bl { left: 10px; bottom: 10px; }
  .grommet--br { right: 10px; bottom: 10px; }

  /* Front label */
  .mascot-art {
    position: absolute; left: 14px; top: 124px; width: 234px; height: 246px;
    background: linear-gradient(180deg, rgba(240,150,120,.35), rgba(180,60,40,.35));
  }
  .brand-column {
    position: absolute; right: 12px; top: 54px; width: 160px;
    display: flex; flex-direction: column; align-items: center;
    font-family: "Rubik Dirt", sans-serif; color: var(--chalk);
    font-size: 168px; line-height: 172px;
  }
  .features {
    position: absolute; left: 14px; top: 420px; list-style: none;
    color: var(--ink); font-weight: 700; font-size: 31px; font-variant: small-caps;
    letter-spacing: 0.5px; white-space: nowrap;
  }
  .features li { height: 63px; }
  .pants-art {
    position: absolute; left: 32px; top: 682px; width: 144px; height: 144px; border-radius: 50%;
    background: radial-gradient(circle, #3a2a24 0%, #1a0f0c 100%);
  }
  .product-line {
    position: absolute; left: 10px; right: 10px; top: 896px; text-align: center;
    font-family: "Big Shoulders Stencil Display", sans-serif; font-weight: 900;
    color: var(--ink); font-size: 76px; line-height: 80px; letter-spacing: 2px; white-space: nowrap;
  }

  /* Back label */
  .cert-badge {
    position: absolute; left: 110px; top: 140px; width: 184px; height: 184px; border-radius: 50%;
    border: 6px solid var(--ink);
  }
  .plant-statement {
    position: absolute; left: 10px; right: 10px; top: 370px; text-align: center;
    color: var(--chalk); font-weight: 600; font-size: 28px; line-height: 53px; text-transform: uppercase;
  }
  .eco-stamp {
    position: absolute; left: 24px; top: 800px; width: 356px; height: 176px;
    border: 8px solid var(--ink); border-radius: 24px; transform: rotate(-3deg);
    display: flex; flex-direction: column; align-items: center; justify-content: center;
    font-family: "Big Shoulders Stencil Display", sans-serif; font-weight: 800;
    color: var(--ink); text-transform: uppercase; white-space: nowrap;
  }
  .eco-stamp__line { font-size: 38px; line-height: 40px; }
  .eco-stamp__brand { font-weight: 900; font-size: 64px; line-height: 64px; letter-spacing: 2px; }

  /* Size label */
  .size-icon {
    position: absolute; left: 18px; top: 12px; width: 46px; height: 46px; border-radius: 50%;
    background: #1a0f0c;
  }
  .size-caption {
    position: absolute; left: 68px; top: 16px;
    font-family: "Saira Stencil One", sans-serif; color: var(--ink); font-size: 28px;
  }
  .size-box {
    position: absolute; left: 16px; top: 62px; width: 142px; height: 250px;
    border: 7px solid var(--chalk); border-radius: 22px;
    display: flex; flex-direction: column; align-items: center; justify-content: center;
    font-family: "Saira Stencil One", sans-serif; color: var(--chalk);
  }
  .size-box__num { font-size: 76px; line-height: 82px; }
  .size-box__x { font-size: 40px; line-height: 46px; }
</style>
</head>
<body>
  <section class="label label--front">
    <span class="grommet grommet--tl"></span><span class="grommet grommet--tr"></span>
    <span class="grommet grommet--bl"></span><span class="grommet grommet--br"></span>
    <div class="mascot-art" role="img" aria-label="Line illustration of a moose standing on a rock"></div>
    <div class="brand-column" aria-label="Vantu"><span>V</span><span>A</span><span>N</span><span>T</span><span>U</span></div>
    <ul class="features">
      <li>Comfort fit</li>
      <li>Wrinkle-resistant</li>
      <li>machine washable</li>
      <li>luxury fabric</li>
    </ul>
    <div class="pants-art" role="img" aria-label="Drawing of cargo trousers in a dark circle"></div>
    <h1 class="product-line">MEN'S CARGO</h1>
  </section>

  <section class="label label--back">
    <span class="grommet grommet--tl"></span><span class="grommet grommet--tr"></span>
    <span class="grommet grommet--bl"></span><span class="grommet grommet--br"></span>
    <div class="cert-badge" aria-hidden="true"></div>
    <p class="plant-statement">
      This Vantu cargo<br>was proudly produced<br>in a Quarv<br>platinum certified<br>green plant<br>with no negative<br>enviromental impact
    </p>
    <div class="eco-stamp">
      <span class="eco-stamp__line">Help the enviroment</span>
      <span class="eco-stamp__line">buy a</span>
      <span class="eco-stamp__brand">Vantu</span>
    </div>
  </section>

  <section class="label label--size">
    <div class="size-icon" role="img" aria-label="Small trousers waistband icon"></div>
    <span class="size-caption">SIZE</span>
    <div class="size-box">
      <span class="size-box__num">32</span>
      <span class="size-box__x">X</span>
      <span class="size-box__num">32</span>
    </div>
  </section>
</body>
</html>
```